Independence Day Graphics for Sale

I want to create 10 social media graphics (new Pictora size 4:5 (1080 x 1350 pixels) focusing on our July 4th Sale Graphics, using any of the pics attached. Use the attached pics, NO RANDOM STOCK PHOTOGRAPHY. For the color scheme of the graphics, they should all be complementary to the product colors in the photos.
You can add any of the photos attached but none are required. You can do some of the graphics in all text. I mainly need BOLD text that says one of the headlines (10 total) SEE ATTACHED WORD DOCUMENT for the headlines to use.

Target Market(s)

women looking to lose weight

Requirements
Must have
• pics attached and text attached

```html
<!DOCTYPE html>
<html lang="en">
<head>
<meta charset="utf-8">
<title>Independence Day Sale – Social Graphics</title>
<link rel="stylesheet" href="https://fonts.googleapis.com/css2?family=Abril+Fatface&family=Lato:wght@700&display=swap">
<style>
:root{
  --board:#d7d7d7;
  --label:#1c1c1c;
  --white:#ffffff;
  --magenta:#e02ea4;
  --hot:#f24dbb;
  --deep:#7e0c50;
  --plum:#a3146c;
  --orange:#f89a1c;
  --orange-deep:#e6541f;
}
*{margin:0;padding:0;box-sizing:border-box}
html,body{width:849px;height:1200px;overflow:hidden;background:var(--board)}
.board{position:relative;width:849px;height:1200px}
.card{position:absolute;width:182px;height:227px;overflow:hidden;font-family:"Abril Fatface",serif;color:var(--white)}
.card--pink{background:linear-gradient(160deg,var(--plum) 0%,var(--magenta) 45%,var(--hot) 60%,var(--deep) 100%)}
.card--white{background:var(--white)}
.ring{position:absolute;inset:0;width:182px;height:227px}
.photo{position:absolute}
.photo--model{background:linear-gradient(180deg,rgba(255,255,255,.15),rgba(40,20,30,.35) 40%,rgba(255,255,255,.55) 65%,rgba(30,20,30,.6));border-radius:40px 40px 6px 6px}
.photo--ghost{background:radial-gradient(ellipse at 50% 30%,rgba(255,200,235,.35),rgba(255,255,255,0) 70%)}
.photo--bottles{background:linear-gradient(180deg,#f4f4f4,#e6e3e6);border-radius:4px}
.photo--bottles-pink{background:linear-gradient(180deg,rgba(255,255,255,.55),rgba(255,220,240,.25));border-radius:4px}
.ln{position:absolute;white-space:nowrap;line-height:1}
.grad{background:linear-gradient(180deg,var(--magenta),var(--deep));-webkit-background-clip:text;background-clip:text;color:transparent}
.grad-orange{background:linear-gradient(180deg,var(--orange),var(--orange-deep));-webkit-background-clip:text;background-clip:text;color:transparent}
.off-v{position:absolute;white-space:nowrap;line-height:1;transform:rotate(-90deg);transform-origin:left top}
.pill{position:absolute;background:var(--orange-deep);color:var(--white);border-radius:4px;font-size:9px;line-height:14px;text-align:center}
.label{position:absolute;width:182px;text-align:center;font-family:"Lato",sans-serif;font-weight:700;font-size:8.5px;letter-spacing:2px;color:var(--label)}
.sup{font-size:.4em;vertical-align:top}
</style>
</head>
<body>
<main class="board">

<!-- 01 -->
<section class="card card--pink" style="left:113px;top:77px">
  <svg class="ring" viewBox="0 0 182 227"><circle cx="95" cy="118" r="96" fill="none" stroke="#b0127a" stroke-width="4"/><path d="M10 40 Q40 18 85 20" fill="none" stroke="#f56cc6" stroke-width="4"/></svg>
  <div class="photo photo--model" role="img" aria-label="Smiling woman holding a supplement bottle" style="left:120px;top:57px;width:62px;height:133px"></div>
  <span class="ln" style="left:40px;top:30px;font-size:20px">4<span class="sup" style="font-size:.6em">th</span></span>
  <span class="ln" style="left:22px;top:50px;font-size:40px">July</span>
  <span class="ln" style="left:22px;top:96px;font-size:22px">MEGA</span>
  <span class="ln" style="left:22px;top:120px;font-size:32px">SALE</span>
  <span class="ln" style="left:22px;top:156px;font-size:34px">25%</span>
  <span class="off-v" style="left:110px;top:192px;font-size:13px">OFF</span>
</section>
<div class="label" style="left:113px;top:322px">DESIGN 01</div>

<!-- 02 -->
<section class="card card--pink" style="left:333px;top:77px">
  <div class="photo photo--ghost" role="img" aria-label="Faded photo of woman in kitchen" style="inset:0"></div>
  <svg class="ring" viewBox="0 0 182 227"><circle cx="95" cy="130" r="118" fill="none" stroke="#fff" stroke-width="5"/></svg>
  <span class="ln" style="left:24px;top:41px;font-size:29px">BIGGEST</span>
  <span class="ln" style="left:20px;top:72px;font-size:32px">4</span>
  <span class="ln" style="left:43px;top:74px;font-size:11px">TH<br>OF</span>
  <span class="ln" style="left:66px;top:73px;font-size:30px">JULY</span>
  <span class="ln" style="left:23px;top:106px;font-size:23px">SALE EVER!</span>
  <span class="ln" style="left:20px;top:132px;font-size:50px">25%</span>
  <span class="off-v" style="left:141px;top:182px;font-size:22px">OFF</span>
  <span class="ln" style="left:20px;top:186px;font-size:25px">SITEWIDE</span>
</section>
<div class="label" style="left:333px;top:322px">DESIGN 02</div>

<!-- 03 -->
<section class="card card--white" style="left:554px;top:77px">
  <svg class="ring" viewBox="0 0 182 227"><circle cx="93" cy="118" r="112" fill="none" stroke="var(--magenta)" stroke-width="3"/></svg>
  <span class="ln grad-orange" style="left:18px;top:26px;font-size:44px">MEGA</span>
  <span class="ln grad-orange" style="left:18px;top:71px;font-size:30px">SUMMER</span>
  <span class="ln grad-orange" style="left:18px;top:103px;font-size:26px">BLOWOUT!</span>
  <span class="ln grad" style="left:18px;top:132px;font-size:52px">25%</span>
  <span class="off-v grad" style="left:153px;top:184px;font-size:22px">OFF</span>
  <span class="ln grad" style="left:18px;top:188px;font-size:17px">OF EVERYTHING</span>
</section>
<div class="label" style="left:554px;top:322px">DESIGN 03</div>

<!-- 04 -->
<section class="card card--white" style="left:113px;top:350px">
  <svg class="ring" viewBox="0 0 182 227"><circle cx="91" cy="112" r="116" fill="none" stroke="var(--magenta)" stroke-width="4"/></svg>
  <span class="ln grad" style="left:14px;top:20px;font-size:26px">ONE-TIME</span>
  <span class="ln grad" style="left:14px;top:48px;font-size:46px">ONLY:</span>
  <span class="ln grad" style="left:12px;top:97px;font-size:78px">25</span>
  <span class="ln grad" style="left:126px;top:99px;font-size:48px">%</span>
  <span class="ln grad" style="left:118px;top:150px;font-size:24px">OFF</span>
  <span class="ln grad" style="left:14px;top:180px;font-size:17px">OF EVERYTHING</span>
</section>
<div class="label" style="left:113px;top:595px">DESIGN 04</div>

<!-- 05 -->
<section class="card card--pink" style="left:333px;top:350px">
  <div class="photo photo--ghost" role="img" aria-label="Faded photo of woman in kitchen with supplements" style="inset:0"></div>
  <svg class="ring" viewBox="0 0 182 227"><circle cx="95" cy="118" r="112" fill="none" stroke="#c01a85" stroke-width="5"/></svg>
  <span class="ln" style="left:27px;top:46px;font-size:25px">HISTORIC</span>
  <span class="ln" style="left:22px;top:72px;font-size:46px">4</span>
  <span class="ln" style="left:60px;top:74px;font-size:22px">TH<span style="font-size:.45em">OF</span>JULY</span>
  <span class="ln" style="left:60px;top:97px;font-size:25px">SALE!</span>
  <span class="ln" style="left:16px;top:133px;font-size:52px">25%</span>
  <span class="off-v" style="left:141px;top:187px;font-size:24px">OFF</span>
  <span class="ln" style="left:16px;top:191px;font-size:16px">OF EVERYTHING</span>
</section>
<div class="label" style="left:333px;top:595px">DESIGN 05</div>

<!-- 06 -->
<section class="card card--white" style="left:554px;top:350px">
  <svg class="ring" viewBox="0 0 182 227"><circle cx="91" cy="112" r="110" fill="none" stroke="var(--magenta)" stroke-width="4"/></svg>
  <span class="ln grad" style="left:22px;top:20px;font-size:68px">25</span>
  <span class="ln grad" style="left:118px;top:20px;font-size:38px">%</span>
  <span class="ln grad" style="left:118px;top:70px;font-size:20px">OFF</span>
  <span class="ln grad" style="left:23px;top:95px;font-size:14px">STOCK-UP EVENT:</span>
  <div class="pill" style="left:22px;top:111px;width:138px">25% OFF ALL SUPPLEMENTS</div>
  <div class="photo photo--bottles" role="img" aria-label="Row of four supplement bottles" style="left:16px;top:131px;width:150px;height:80px"></div>
</section>
<div class="label" style="left:554px;top:595px">DESIGN 06</div>

<!-- 07 -->
<section class="card card--pink" style="left:113px;top:623px">
  <svg class="ring" viewBox="0 0 182 227"><circle cx="95" cy="118" r="108" fill="none" stroke="#c01a85" stroke-width="4"/></svg>
  <div class="photo photo--model" role="img" aria-label="Smiling woman holding a supplement bottle" style="left:104px;top:17px;width:70px;height:130px"></div>
  <div class="ln" style="left:20px;top:16px;width:96px;text-align:center;font-size:20px;line-height:21px;white-space:normal">THE<br>LOWEST<br>PRICES<br>WE'VE<br>EVER<br>OFFERED!</div>
  <span class="ln" style="left:22px;top:143px;font-size:68px">25</span>
  <span class="ln" style="left:118px;top:142px;font-size:40px">%</span>
  <span class="ln" style="left:118px;top:191px;font-size:20px">OFF</span>
</section>
<div class="label" style="left:113px;top:868px">DESIGN 07</div>

<!-- 08 -->
<section class="card card--pink" style="left:333px;top:623px">
  <svg class="ring" viewBox="0 0 182 227"><circle cx="91" cy="118" r="110" fill="none" stroke="var(--orange)" stroke-width="4"/></svg>
  <div class="photo photo--bottles-pink" role="img" aria-label="Row of four supplement bottles" style="left:30px;top:17px;width:126px;height:64px"></div>
  <span class="off-v" style="left:18px;top:105px;font-size:8px">OUR</span>
  <span class="ln" style="left:28px;top:86px;font-size:30px">BIGGEST</span>
  <span class="ln" style="left:17px;top:116px;font-size:17px">DISCOUNT EVER!</span>
  <span class="ln" style="left:16px;top:135px;font-size:52px">25%</span>
  <span class="off-v" style="left:141px;top:188px;font-size:24px">OFF</span>
  <span class="ln" style="left:16px;top:193px;font-size:17px">OF EVERYTHING</span>
</section>
<div class="label" style="left:333px;top:868px">DESIGN 08</div>

<!-- 09 -->
<section class="card card--pink" style="left:554px;top:623px">
  <div class="photo photo--ghost" role="img" aria-label="Faded photo of woman holding a supplement bottle" style="left:90px;top:0;width:92px;height:227px"></div>
  <svg class="ring" viewBox="0 0 182 227"><circle cx="91" cy="118" r="112" fill="none" stroke="#b0127a" stroke-width="4"/></svg>
  <span class="ln" style="left:16px;top:28px;font-size:44px">DON'T</span>
  <span class="ln" style="left:18px;top:74px;font-size:44px">WAIT!</span>
  <span class="ln" style="left:18px;top:124px;font-size:52px">25%</span>
  <span class="off-v" style="left:150px;top:178px;font-size:22px">OFF</span>
  <span class="ln" style="left:18px;top:184px;font-size:23px">ENDS SOON</span>
</section>
<div class="label" style="left:554px;top:868px">DESIGN 09</div>

<!-- 10 -->
<section class="card card--white" style="left:113px;top:896px">
  <svg class="ring" viewBox="0 0 182 227"><circle cx="91" cy="112" r="114" fill="none" stroke="var(--magenta)" stroke-width="4"/></svg>
  <span class="ln grad" style="left:16px;top:20px;font-size:48px">LAST</span>
  <span class="ln grad" style="left:12px;top:70px;font-size:35px">CHANCE</span>
  <span class="ln grad" style="left:12px;top:108px;font-size:76px">25</span>
  <span class="ln grad" style="left:126px;top:108px;font-size:44px">%</span>
  <span class="ln grad" style="left:118px;top:162px;font-size:24px">OFF</span>
  <span class="ln grad" style="left:14px;top:191px;font-size:13px">TIME IS RUNNING OUT!</span>
</section>
<div class="label" style="left:113px;top:1141px">DESIGN 10</div>

<!-- 11 -->
<section class="card card--pink" style="left:333px;top:896px">
  <div class="photo photo--ghost" role="img" aria-label="Faded photo of kitchen with supplements" style="inset:0"></div>
  <svg class="ring" viewBox="0 0 182 227"><circle cx="91" cy="112" r="114" fill="none" stroke="#c9c9c9" stroke-width="4"/></svg>
  <span class="ln" style="left:16px;top:20px;font-size:48px">LAST</span>
  <span class="ln" style="left:12px;top:70px;font-size:35px">CHANCE</span>
  <span class="ln" style="left:12px;top:108px;font-size:76px">25</span>
  <span class="ln" style="left:126px;top:108px;font-size:44px">%</span>
  <span class="ln" style="left:118px;top:162px;font-size:24px">OFF</span>
  <span class="ln" style="left:14px;top:191px;font-size:13px">TIME IS RUNNING OUT!</span>
</section>
<div class="label" style="left:333px;top:1141px">DESIGN 11</div>

<!-- 12 -->
<section class="card card--pink" style="left:554px;top:896px">
  <svg class="ring" viewBox="0 0 182 227"><circle cx="95" cy="118" r="108" fill="none" stroke="#b0127a" stroke-width="4"/></svg>
  <div class="photo photo--model" role="img" aria-label="Smiling woman holding a supplement bottle" style="left:112px;top:39px;width:70px;height:178px"></div>
  <span class="ln" style="left:13px;top:18px;font-size:40px">LAST</span>
  <span class="ln" style="left:11px;top:57px;font-size:27px">CHANCE</span>
  <span class="ln" style="left:11px;top:88px;font-size:34px">25%</span>
  <span class="off-v" style="left:86px;top:122px;font-size:14px">OFF</span>
  <span class="ln" style="left:16px;top:128px;font-size:27px">TIME<span style="font-size:.45em">IS</span></span>
  <span class="ln" style="left:13px;top:157px;font-size:22px">RUNNING</span>
  <span class="ln" style="left:26px;top:182px;font-size:27px">OUT!</span>
</section>
<div class="label" style="left:554px;top:1141px">DESIGN 12</div>

</main>
</body>
</html>
```